Brightvale services brochure

We need a new company brochure. The brochure will be formatted for PDF distribution but should be printable on "letter" size paper. 2 pages plus front and back cover. Color white and same blue as logo. Logo "O" should be used as design. Look at webpage for general info: www.brightvale-example.ca<br/><br/>Front cover: pic1, logo, design and "Your Cleaning is Our Business". <br/>Back cover" "O" design, logo and info from "contact" page<br/>Front cover inside: design and intro from web home page, also use stock pics of clean offices ect as placeholders for purchased pics.<br/>1st page: design and "Our Services", use info of "Cleanroom & GMP Services", "Janitorial Services" from services page.<br/>2nd page: design and "Special Services", info from "Carpet & Upholstery Services", "Window Cleaning Services", and list of "Other Services".<br/>Back cover inside : design and info from technology page, use stock pics for place holders.

Industry/Entity Type

Janitorial

Font styles to use
Sans Serif
Other font styles liked:
• Futura Book

Colors
0555a3

Requirements
Must have
• The logo "O" (target) should be part of the design. Design color same as logo.

```html
<!DOCTYPE html>
<html lang="en">
<head>
<meta charset="utf-8">
<title>Brightvale Building Services – Brochure</title>
<link rel="stylesheet" href="https://fonts.googleapis.com/css2?family=Montserrat:ital,wght@0,400;0,500;0,600;0,700;0,800;1,800&display=swap">
<style>
  :root {
    --brand-blue: #0b74c4;
    --brand-blue-deep: #0555a3;
    --ink: #1b1b22;
    --muted: #4a4a52;
    --backdrop: #585858;
    --paper: #ffffff;
    --card-grey: #f1f2f4;
  }
  * { margin: 0; padding: 0; box-sizing: border-box; }
  html, body { width: 668px; height: 1200px; overflow: hidden; }
  body {
    background: var(--backdrop);
    font-family: "Montserrat", sans-serif;
    color: var(--ink);
    position: relative;
  }
  .page {
    position: absolute;
    width: 272px;
    height: 352px;
    background: var(--paper);
    overflow: hidden;
  }
  .page > svg.page-shapes { position: absolute; inset: 0; width: 272px; height: 352px; }
  .abs { position: absolute; }

  .front-cover { left: 188px; top: 50px; }
  .services-page { left: 53px; top: 432px; }
  .other-services-page { left: 342px; top: 432px; }
  .back-cover { left: 206px; top: 814px; }

  .brand-name {
    color: var(--brand-blue);
    font-weight: 500;
    letter-spacing: 0.14em;
    white-space: nowrap;
  }

  /* Front cover */
  .front-cover .brand-name { left: 0; width: 272px; top: 26px; text-align: center; font-size: 19px; }
  .cover-tagline { left: 0; width: 272px; top: 253px; text-align: center; color: #fff; }
  .cover-tagline .lead { display: block; font-size: 14px; font-weight: 500; letter-spacing: 0.2em; line-height: 16px; }
  .cover-tagline .strong { display: block; font-size: 24.5px; font-weight: 800; letter-spacing: 0.02em; line-height: 26px; }
  .cover-url { left: 0; width: 272px; top: 331px; text-align: center; font-size: 6px; letter-spacing: 0.28em; font-weight: 600; }
  .cover-url span { color: var(--brand-blue); font-weight: 500; }

  /* Section headings */
  .section-heading {
    font-size: 13px; letter-spacing: 0.32em; font-weight: 500; white-space: nowrap;
    border-left: 2px solid var(--brand-blue); padding-left: 8px; line-height: 12px;
  }
  .section-heading b { color: var(--brand-blue); font-weight: 600; }
  .services-page .section-heading { left: 24px; top: 25px; }
  .other-services-page .section-heading { left: 29px; top: 25px; }

  /* Service list */
  .service-icon {
    width: 30px; height: 30px; border-radius: 50%; background: #fff;
    border: 1px solid #e2e4e8; box-shadow: -4px 3px 6px rgba(0,0,0,0.12);
    display: flex; align-items: center; justify-content: center;
  }
  .service-icon i { width: 14px; height: 16px; border-radius: 3px; background: var(--brand-blue); display: block; }
  .service-item { left: 67px; width: 190px; }
  .service-item h3 { font-size: 7.4px; font-weight: 500; color: var(--brand-blue-deep); line-height: 9px; }
  .service-item p { font-size: 3.9px; line-height: 5.5px; color: var(--muted); margin-top: 2px; }

  .program-note { left: 25px; top: 274px; width: 225px; color: #fff; }
  .program-note h4 {
    font-size: 7.8px; font-weight: 500; line-height: 10px; border-left: 1.5px solid #fff; padding-left: 9px; margin-left: 0;
  }
  .program-note p { font-size: 5.9px; line-height: 8.7px; padding-left: 10px; margin-top: 3px; color: #e3efff; }
  .program-note p b { font-weight: 600; color: #fff; }

  /* Other services */
  .other-list { left: 30px; top: 49px; list-style: none; }
  .other-list li { font-size: 7.4px; line-height: 13.25px; white-space: nowrap; font-weight: 500; }
  .other-list li::before { content: "»"; color: var(--brand-blue); font-weight: 700; margin-right: 6px; }

  .offers-title {
    left: 28px; top: 240px; width: 220px; height: 17.5px; background: #fff; border-radius: 1.5px;
    text-align: center; font-size: 9.5px; font-weight: 700; line-height: 17.5px; letter-spacing: 0.02em;
  }
  .offer-card {
    top: 267px; width: 52px; height: 68px; background: var(--card-grey); border-radius: 1.5px;
    text-align: center; overflow: hidden;
  }
  .offer-card .label { height: 26px; display: flex; align-items: center; justify-content: center; font-size: 5px; line-height: 6px; font-weight: 500; padding: 0 3px; }
  .offer-card .value { height: 19px; background: var(--brand-blue-deep); color: #fff; font-size: 11px; font-weight: 700; line-height: 19px; }
  .offer-card .note { height: 23px; display: flex; align-items: center; justify-content: center; font-size: 4.2px; line-height: 5px; font-weight: 500; text-transform: uppercase; padding: 0 2px; }

  /* Back cover */
  .availability { left: 35px; top: 186px; color: #fff; }
  .availability .line-strong { font-size: 14px; font-weight: 700; line-height: 16px; display: block; letter-spacing: 0.01em; }
  .availability .line { font-size: 10.6px; font-weight: 500; line-height: 14px; display: block; }
  .availability .line.wide { letter-spacing: 0.02em; }
  .round-the-clock { left: 155px; top: 174px; color: #fff; font-size: 33px; font-weight: 800; font-style: italic; letter-spacing: -0.04em; line-height: 36px; }

  .contact-heading { left: 35px; top: 271px; font-size: 8px; font-weight: 700; }
  .contact-heading b { color: var(--brand-blue); font-weight: 700; }
  .contact-heading::after { content: ""; display: block; width: 6px; height: 1px; background: var(--brand-blue); margin-top: 3px; }
  .contact-list { left: 29px; top: 288px; list-style: none; }
  .contact-list li { font-size: 6px; line-height: 11.8px; font-weight: 500; display: flex; align-items: center; }
  .contact-list svg { width: 5px; height: 5px; margin-right: 2.5px; }
  .back-cover .brand-name { left: 160px; top: 299px; width: 90px; text-align: center; font-size: 9.5px; }
  .social-row { left: 204px; top: 325px; display: flex; gap: 4px; }
  .social-row span { width: 7px; height: 7px; border-radius: 50%; background: var(--brand-blue-deep); display: block; }
</style>
</head>
<body>

<!-- Front cover -->
<section class="page front-cover">
  <svg class="page-shapes" viewBox="0 0 272 352" aria-hidden="false">
    <defs>
      <linearGradient id="buildingTones" x1="0" y1="0" x2="0" y2="1">
        <stop offset="0" stop-color="#ffffff"/>
        <stop offset="0.25" stop-color="#dce8f0"/>
        <stop offset="0.7" stop-color="#a9bccb"/>
        <stop offset="1" stop-color="#6f8a6a"/>
      </linearGradient>
      <linearGradient id="coverBlue" x1="0" y1="0" x2="0" y2="1">
        <stop offset="0" stop-color="#0b74c4"/>
        <stop offset="1" stop-color="#0a6abb"/>
      </linearGradient>
    </defs>
    <rect x="0" y="58" width="272" height="190" fill="url(#buildingTones)" role="img" aria-label="Photo of a modern glass office tower with palm trees at its base"/>
    <path d="M0 171 Q 110 262 272 213 L272 275 Q 150 345 0 297 Z" fill="url(#coverBlue)"/>
  </svg>
  <div class="abs brand-name">BRIGHTVALE</div>
  <h1 class="abs cover-tagline"><span class="lead">YOUR CLEANING IS</span><span class="strong">OUR BUSINESS</span></h1>
  <div class="abs cover-url">www.<span>brightvale-example</span>.ca</div>
</section>

<!-- Inside left: Our Services -->
<section class="page services-page">
  <svg class="page-shapes" viewBox="0 0 272 352">
    <defs>
      <linearGradient id="swooshGrey" x1="0" y1="0" x2="1" y2="0">
        <stop offset="0" stop-color="#ffffff"/>
        <stop offset="0.5" stop-color="#cfcfd2"/>
        <stop offset="1" stop-color="#8c8c90"/>
      </linearGradient>
      <linearGradient id="panelBlue" x1="0" y1="0" x2="0" y2="1">
        <stop offset="0" stop-color="#0b74c4"/>
        <stop offset="1" stop-color="#0555a3"/>
      </linearGradient>
    </defs>
    <path d="M0 236 Q 130 290 272 219 L272 228 Q 140 288 0 243 Z" fill="url(#swooshGrey)"/>
    <path d="M0 243 Q 135 293 272 228 L272 352 L0 352 Z" fill="url(#panelBlue)"/>
  </svg>
  <h2 class="abs section-heading">OUR <b>SERVICES</b></h2>

  <div class="abs service-icon" style="left:28px;top:49px" role="img" aria-label="Janitor with cleaning cart icon"><i></i></div>
  <div class="abs service-item" style="top:48px">
    <h3>Janitorial Services</h3>
    <p>Brightvale provides complete janitorial services for any type/size operation. We currently service the public and private sectors, offices, financial institutions, industrial plants, schools, apartment buildings, showrooms, churches, as well as many other facilities.</p>
  </div>

  <div class="abs service-icon" style="left:28px;top:88px" role="img" aria-label="Cleaner with mop and bucket icon"><i></i></div>
  <div class="abs service-item" style="top:87px">
    <h3>Cleanroom &amp; GMP Services</h3>
    <p>Brightvale is a leading brand in cleanroom cleaning and boasts an impressive performance record. The company is recognized as a reliable, mature organization, continually adjusting and perfecting the systems and methodologies used to bring cleanroom cleaning procedures and technology to businesses worldwide.</p>
  </div>

  <div class="abs service-icon" style="left:28px;top:128px" role="img" aria-label="Cleaner vacuuming carpet icon"><i></i></div>
  <div class="abs service-item" style="top:130px">
    <h3>Carpet &amp; Upholstery Services</h3>
    <p>Office furnishings such as carpets, drapes and upholstered furniture represent a serious investment to a company. We maintain this investment with care and quality that extends the lifespan of furniture and carpet.</p>
  </div>

  <div class="abs service-icon" style="left:28px;top:169px" role="img" aria-label="Window cleaner icon"><i></i></div>
  <div class="abs service-item" style="top:170px">
    <h3>Window Cleaning Services</h3>
    <p>We can implement a regular program of interior and exterior window cleaning, or we can meet your needs as a project basis. We have the staff and equipment to tackle both high-rise and low level window cleaning.</p>
  </div>

  <div class="abs service-icon" style="left:28px;top:209px" role="img" aria-label="Restoration worker icon"><i></i></div>
  <div class="abs service-item" style="top:210px">
    <h3>Fire And Flood Restoration Services</h3>
    <p>No one can anticipate when a fire, accident, natural disaster or vandalism will devastate or deface your building. Even something as simple as smoke damage can change a tenant's experience within a building.</p>
  </div>

  <div class="abs program-note">
    <h4>SPECIAL 2019<br>NOVEL CORONAVIRUS DISINFECTING PROGRAM</h4>
    <p>With the global spreading of the 2019 <b>Novel Coronavirus (2019-nCoV)</b>, Brightvale offers preventive disinfecting programs to ensure facilities are properly disinfected.<br>Contact us for a program that fits your needs.</p>
  </div>
</section>

<!-- Inside right: Other Services -->
<section class="page other-services-page">
  <svg class="page-shapes" viewBox="0 0 272 352">
    <defs>
      <linearGradient id="swooshGreyRight" x1="0" y1="0" x2="1" y2="0">
        <stop offset="0" stop-color="#ffffff"/>
        <stop offset="0.5" stop-color="#d6d6d9"/>
        <stop offset="1" stop-color="#86868a"/>
      </linearGradient>
      <linearGradient id="panelBlueRight" x1="0" y1="0" x2="0" y2="1">
        <stop offset="0" stop-color="#0b74c4"/>
        <stop offset="1" stop-color="#0866b6"/>
      </linearGradient>
      <linearGradient id="portraitTones" x1="0" y1="0" x2="1" y2="1">
        <stop offset="0" stop-color="#e9ecef"/>
        <stop offset="0.6" stop-color="#c9c3bb"/>
        <stop offset="1" stop-color="#b7b2ab"/>
      </linearGradient>
    </defs>
    <path d="M0 232 Q 135 160 272 213 L272 227 Q 137 170 0 240 Z" fill="url(#swooshGreyRight)"/>
    <path d="M0 240 Q 137 172 272 227 L272 352 L0 352 Z" fill="url(#panelBlueRight)"/>
    <circle cx="221" cy="90" r="56" fill="url(#portraitTones)" role="img" aria-label="Photo of a smiling cleaner in yellow gloves wiping a window"/>
    <circle cx="221" cy="90" r="58" fill="none" stroke="#0b74c4" stroke-width="0.8"/>
  </svg>
  <h2 class="abs section-heading">OTHER <b>SERVICES</b></h2>
  <ul class="abs other-list">
    <li>Day Porter Services</li>
    <li>Construction Clean-Ups</li>
    <li>Quality Control Inspections</li>
    <li>Maid Services</li>
    <li>Light &amp; Ceiling Fixture Cleaning</li>
    <li>Wall Washing</li>
    <li>Drapery &amp; Blind Cleaning</li>
    <li>Acoustical Tile Cleaning</li>
    <li>Computer Terminal, Monitor and Keyboard Cleaning</li>
    <li>Marble, Granite &amp; Terrazzo Refinishing &amp; Maintenance</li>
    <li>Power Washing</li>
  </ul>

  <div class="abs offers-title">OUR SPECIAL OFFERS</div>
  <div class="abs offer-card" style="left:28px"><div class="label">All<br>Estimates</div><div class="value">FREE</div><div class="note"></div></div>
  <div class="abs offer-card" style="left:84px"><div class="label">New Janitorial<br>Contracts</div><div class="value">FREE</div><div class="note">Carpet<br>Cleaning</div></div>
  <div class="abs offer-card" style="left:140px"><div class="label">Janitorial<br>Supplies</div><div class="value">FREE</div><div class="note">Delivery</div></div>
  <div class="abs offer-card" style="left:196px"><div class="label">Starting at</div><div class="value">$95</div><div class="note">Carpet<br>Maintenance<br>Program</div></div>
</section>

<!-- Back cover -->
<section class="page back-cover">
  <svg class="page-shapes" viewBox="0 0 272 352">
    <defs>
      <linearGradient id="wipeTones" x1="0" y1="0" x2="1" y2="1">
        <stop offset="0" stop-color="#eef3f7"/>
        <stop offset="0.45" stop-color="#6fb8df"/>
        <stop offset="0.7" stop-color="#9a5535"/>
        <stop offset="1" stop-color="#c7c9cc"/>
      </linearGradient>
      <linearGradient id="backBlue" x1="0" y1="0" x2="0" y2="1">
        <stop offset="0" stop-color="#0b74c4"/>
        <stop offset="1" stop-color="#0a6bbb"/>
      </linearGradient>
    </defs>
    <rect x="0" y="0" width="272" height="180" fill="url(#wipeTones)" role="img" aria-label="Photo of a blue-gloved hand wiping a wooden drawer with a cloth"/>
    <path d="M0 87 Q 110 200 272 138 L272 210 Q 150 290 0 231 Z" fill="url(#backBlue)"/>
    <path d="M211 178 A 26 26 0 0 1 226 212" fill="none" stroke="#fff" stroke-width="1.6"/>
  </svg>
  <div class="abs availability">
    <span class="line-strong">AT BRIGHTVALE</span>
    <span class="line">WE ARE AVAILABLE</span>
    <span class="line wide">FOR SUPPORTING OUR CLIENTS.</span>
  </div>
  <div class="abs round-the-clock">24/7</div>

  <h2 class="abs contact-heading">CONTACT <b>BRIGHTVALE</b></h2>
  <ul class="abs contact-list">
    <li><svg viewBox="0 0 10 10"><circle cx="5" cy="5" r="4" fill="none" stroke="#0555a3" stroke-width="1.2"/><path d="M3.5 3 L4.5 3 L4.8 4.5 L4.2 5 Q5 6.2 6 6.5 L6.5 6 L7 7 L6.5 7.5 Q4 7 3 4 Z" fill="#0555a3"/></svg>1 (800) 555-0142</li>
    <li><svg viewBox="0 0 10 10"><rect x="2" y="2" width="6" height="6" rx="1" fill="#0555a3"/></svg>(555) 010-4556</li>
    <li><svg viewBox="0 0 10 10"><rect x="1.5" y="2.5" width="7" height="5" fill="none" stroke="#0555a3" stroke-width="1"/><path d="M1.5 2.5 L5 5.5 L8.5 2.5" fill="none" stroke="#0555a3" stroke-width="1"/></svg>info@brightvale-example.ca</li>
    <li><svg viewBox="0 0 10 10"><circle cx="5" cy="5" r="3.8" fill="none" stroke="#0555a3" stroke-width="1"/><path d="M1.2 5 H8.8 M5 1.2 V8.8" stroke="#0555a3" stroke-width="0.8"/></svg>www.brightvale-example.ca</li>
  </ul>
  <div class="abs brand-name">BRIGHTVALE</div>
  <div class="abs social-row" aria-hidden="true"><span></span><span></span><span></span></div>
</section>

</body>
</html>
```